New business card for civil engineering company - "Keystone Audit"

We need a business card designed for our new structural engineering company.

The company name is "Keystone Audit" logo files attached.

We would like the following:
* Two-sided card
* Simple design

Information to be placed on the card:
Name - Marcus Dellow
Job Title - Director / Structural Engineer
Credentials - BEng(Hons), CPEng, CMengNZ, IntPE(NZ)
Email - marcus.dellow@keystoneaudit.co.nz
mobile - 0219364058
website - www.keystoneaudit.co.nz

```html
<!DOCTYPE html>
<html lang="en">
<head>
<meta charset="utf-8">
<title>Keystone Audit — Business Card</title>
<link rel="stylesheet" href="https://fonts.googleapis.com/css2?family=Lato:wght@400;700&display=swap">
<style>
  :root {
    --backdrop: #2a2a2a;
    --card: #050505;
    --edge: #2f86c8;
    --glow: rgba(47, 134, 200, 0.45);
    --accent: #3a8fd6;
    --accent-soft: #5aa6e6;
    --ink: #e6e6e6;
    --ink-muted: #bdbdbd;
    --brand: #d9d9d9;
  }
  * { box-sizing: border-box; margin: 0; padding: 0; }
  html, body {
    width: 1200px; height: 997px; overflow: hidden;
    background: var(--backdrop);
    font-family: "Lato", Arial, sans-serif;
  }
  .canvas {
    position: relative; width: 1200px; height: 997px;
    display: flex; flex-direction: column; align-items: center; justify-content: center; gap: 70px;
  }
  .card {
    position: relative; width: 720px; height: 400px;
    background: var(--card);
    border: 2px solid var(--edge);
    box-shadow: 0 0 10px var(--glow), 0 18px 40px rgba(0,0,0,0.6);
  }
  .card--back { border-radius: 0 70px 0 70px; display: flex; align-items: center; justify-content: center; }
  .card--front { border-radius: 70px 0 70px 0; display: flex; }

  .brand { display: flex; align-items: center; gap: 14px; }
  .brand__mark { width: 22px; height: 22px; background: var(--brand); }
  .brand__name {
    font-weight: 700; color: var(--brand); letter-spacing: 3px; text-transform: uppercase;
  }
  .card--back .brand__name { font-size: 40px; }
  .card--front .brand__name { font-size: 26px; }
  .card--front .brand__mark { width: 16px; height: 16px; }

  .front__brand-zone { width: 330px; display: flex; align-items: center; justify-content: center; }
  .front__divider {
    width: 2px; margin: 60px 0;
    background: linear-gradient(to bottom, transparent, var(--accent-soft), transparent);
    box-shadow: 0 0 8px var(--glow);
  }
  .front__details { flex: 1; padding: 78px 0 0 40px; }
  .person__name { font-size: 26px; color: var(--accent); font-weight: 700; }
  .person__name .surname { font-weight: 400; color: var(--accent-soft); }
  .person__credentials { font-size: 15px; color: var(--ink); margin-top: 4px; }
  .person__role { font-size: 16px; color: var(--accent); margin-top: 2px; }
  .contact { list-style: none; margin-top: 38px; }
  .contact__item {
    display: flex; align-items: center; gap: 14px;
    font-size: 18px; color: var(--ink-muted); margin-bottom: 10px;
  }
  .contact__icon { width: 18px; height: 18px; fill: var(--accent); flex: none; }
</style>
</head>
<body>
  <main class="canvas">
    <section class="card card--back" aria-label="Card back">
      <div class="brand">
        <span class="brand__mark"></span>
        <span class="brand__name">Keystone Audit</span>
      </div>
    </section>

    <section class="card card--front" aria-label="Card front">
      <div class="front__brand-zone">
        <div class="brand">
          <span class="brand__mark"></span>
          <span class="brand__name">Keystone Audit</span>
        </div>
      </div>
      <div class="front__divider"></div>
      <div class="front__details">
        <h1 class="person__name">Marcus <span class="surname">Dellow</span></h1>
        <p class="person__credentials">BEng(Hons), CPEng, CMengNZ, IntPE(NZ)</p>
        <p class="person__role">Director/ Structural Engineer</p>
        <ul class="contact">
          <li class="contact__item">
            <svg class="contact__icon" viewBox="0 0 24 24"><path d="M3 8c0-2 2-4 9-4s9 2 9 4v2h-5V8H8v2H3z M6 11h12l2 9H4z M12 13a3 3 0 1 0 0.01 0z"/></svg>
            0219364058
          </li>
          <li class="contact__item">
            <svg class="contact__icon" viewBox="0 0 24 24"><path d="M2 5h20v14H2z M4 7v1l8 5 8-5V7l-8 5z" fill-rule="evenodd"/></svg>
            marcus.dellow@keystoneaudit.co.nz
          </li>
          <li class="contact__item">
            <svg class="contact__icon" viewBox="0 0 24 24"><path d="M12 2a10 10 0 1 0 0.01 0z M4.1 11h3.9c.1-2.6.6-5 1.5-6.6A8 8 0 0 0 4.1 11z M10 11h4c-.2-3.3-1.1-6-2-6s-1.8 2.7-2 6z M16 11h3.9a8 8 0 0 0-5.4-6.6c.9 1.6 1.4 4 1.5 6.6z M4.1 13a8 8 0 0 0 5.4 6.6c-.9-1.6-1.4-4-1.5-6.6z M10 13c.2 3.3 1.1 6 2 6s1.8-2.7 2-6z M16 13c-.1 2.6-.6 5-1.5 6.6a8 8 0 0 0 5.4-6.6z" fill-rule="evenodd"/></svg>
            www.keystoneaudit.co.nz
          </li>
        </ul>
      </div>
    </section>
  </main>
</body>
</html>
```